Estate Planner needs an Ad for a local newsletter

I need an ad designed for my practice as an estate planning attorney. The ad will be in a newsletter that targets individuals over the age of 55. My ad is 7.5"W x 4.6"H (a half page ad) .
The wording should include:
Varnholt, Danielle

Danielle Varnholt

Wisdom Meets Planning
Your Estate, Your Legacy

After 23 years as a military spouse, moving our family of six across the country,
I learned the true value of careful planning. Today I help Palomar County's seniors protect what matters most – their family’s future and their life’s work.

I understand that your estate is more than just assets – it's a lifetime of wise
decisions, cherished memories, and dreams for your family's future.

Professional Estate Planning:
• Wills & Living Trusts • Healthcare Directives
• Power of Attorney • Asset Protection
• Probate Avoidance • Peace of Mind

Plus also needs to have my contact information:
RPV Law
Danielle Varnholt
Attorney/Of Counsel
4712 Cedarbrook Lane
Lakemont, Eastvale 00512
(555) 684-1093
dvarnholt@rpvlegalteam.example
Logo is attached.

```html
<!DOCTYPE html>
<html lang="en">
<head>
<meta charset="utf-8">
<title>RPV Law – Estate Planning Ad</title>
<link href="https://fonts.googleapis.com/css2?family=Montserrat:wght@400;500;700;800;900&display=swap" rel="stylesheet">
<style>
  :root {
    --page-bg: #e6e5e6;
    --navy: #1e1f4f;
    --red: #c4172f;
    --blue: #0f4d8a;
    --blue-light: #1f62a3;
    --panel: #f4f5f8;
    --ink: #1c1c24;
    --tick: #c9cacd;
    --white: #ffffff;
  }
  * { margin: 0; padding: 0; box-sizing: border-box; }
  html, body {
    width: 896px; height: 1200px; overflow: hidden;
    background: var(--page-bg);
    font-family: "Montserrat", Arial, sans-serif;
  }
  .ad {
    position: absolute; left: 18px; top: 336px;
    width: 860px; height: 527px;
    background: var(--white);
    overflow: hidden;
  }
  .hero-art { position: absolute; left: 0; top: 0; width: 860px; height: 286px; }
  .firm-name {
    position: absolute; left: 45px; top: 18px;
    display: flex; align-items: center; gap: 8px;
    font-size: 25px; font-weight: 700; color: var(--navy); letter-spacing: 0.5px;
  }
  .firm-name .mark { width: 14px; height: 14px; background: var(--blue); }
  .firm-subline {
    position: absolute; left: 45px; top: 52px;
    font-size: 7px; font-weight: 500; color: var(--navy);
  }
  .headline {
    position: absolute; left: 44px; top: 83px;
    font-weight: 900; font-size: 29px; line-height: 32px;
    text-transform: uppercase; letter-spacing: 0.2px;
  }
  .headline .lead { color: var(--navy); display: block; }
  .headline .accent { color: var(--red); display: block; }
  .intro {
    position: absolute; left: 45px; top: 215px; width: 292px;
    font-size: 9.6px; line-height: 12.6px; color: var(--ink);
    text-align: justify;
  }
  .promise-band {
    position: absolute; left: 0; top: 290px; width: 860px; height: 64px;
    background: var(--blue); color: var(--white);
    display: flex; flex-direction: column; justify-content: center; align-items: center;
    font-size: 16.5px; line-height: 23px; font-weight: 400;
  }
  .services { position: absolute; left: 48px; top: 376px; }
  .services-title {
    font-size: 20px; font-weight: 900; color: var(--red);
    text-transform: uppercase; letter-spacing: 0.2px;
  }
  .service-list {
    list-style: none; margin-top: 10px;
    display: grid; grid-template-columns: 210px 210px; row-gap: 7px;
    grid-auto-flow: column; grid-template-rows: repeat(3, 19px);
  }
  .service-list li {
    display: flex; align-items: center; gap: 10px;
    font-size: 16.5px; color: var(--ink);
  }
  .service-list svg { width: 13px; height: 13px; flex: none; }
  .contact-panel {
    position: absolute; left: 494px; top: 354px; width: 366px; height: 173px;
    background: var(--panel);
    padding: 22px 0 0 40px;
  }
  .attorney-name { font-size: 27px; font-weight: 700; color: var(--blue); line-height: 30px; }
  .attorney-role { font-size: 14.5px; color: var(--navy); margin-top: 1px; }
  .contact-lines { list-style: none; margin-top: 10px; }
  .contact-lines li {
    display: flex; align-items: center; gap: 10px;
    font-size: 10.8px; color: var(--navy); height: 16px;
  }
  .contact-lines li.phone { font-size: 21px; font-weight: 800; color: var(--blue); height: 25px; }
  .contact-lines svg { width: 12px; height: 12px; flex: none; }
</style>
</head>
<body>
<article class="ad">
  <svg class="hero-art" viewBox="0 0 860 286">
    <defs>
      <linearGradient id="parkTones" x1="0" y1="0" x2="0" y2="1">
        <stop offset="0" stop-color="#4f6f32"/>
        <stop offset="0.55" stop-color="#6f8d45"/>
        <stop offset="1" stop-color="#7fa04f"/>
      </linearGradient>
    </defs>
    <polygon class="chevron-band" points="318,0 360,0 443,143 360,286 327,286 405,143" fill="var(--blue)"/>
    <polygon class="chevron-shade" points="340,0 360,0 443,143 360,286 345,286 425,143" fill="var(--blue-light)"/>
    <polygon class="family-photo" points="360,0 860,0 860,286 360,286 443,143" fill="url(#parkTones)"
      role="img" aria-label="Photo: a military family of four walking hand in hand through a sunny park, seen from behind"/>
  </svg>

  <div class="firm-name"><span>RPV Law</span><span class="mark"></span></div>
  <div class="firm-subline">Rowan · Pellham · Vance &nbsp;·&nbsp; EST. 1976</div>

  <h1 class="headline">
    <span class="lead">Wisdom Meets</span>
    <span class="lead">Planning</span>
    <span class="accent">Your Estate,</span>
    <span class="accent">Your Legacy</span>
  </h1>

  <p class="intro">After 23 years as a military spouse, moving our family of six across the country, I learned the true value of careful planning. Today I help Palomar County's seniors protect what matters most – their family’s future and their life’s work.</p>

  <div class="promise-band">
    <span>I understand that your estate is more than just assets –</span>
    <span>it's a lifetime of wise decisions, cherished memories, and dreams for your family's future.</span>
  </div>

  <section class="services">
    <h2 class="services-title">Professional Estate Planning</h2>
    <ul class="service-list">
      <li><svg viewBox="0 0 12 12"><path d="M1 6.5 4.5 10 11 2" fill="none" stroke="var(--tick)" stroke-width="2"/></svg>Wills &amp; Living Trusts</li>
      <li><svg viewBox="0 0 12 12"><path d="M1 6.5 4.5 10 11 2" fill="none" stroke="var(--tick)" stroke-width="2"/></svg>Power of Attorney</li>
      <li><svg viewBox="0 0 12 12"><path d="M1 6.5 4.5 10 11 2" fill="none" stroke="var(--tick)" stroke-width="2"/></svg>Probate Avoidance</li>
      <li><svg viewBox="0 0 12 12"><path d="M1 6.5 4.5 10 11 2" fill="none" stroke="var(--tick)" stroke-width="2"/></svg>Healthcare Directives</li>
      <li><svg viewBox="0 0 12 12"><path d="M1 6.5 4.5 10 11 2" fill="none" stroke="var(--tick)" stroke-width="2"/></svg>Asset Protection</li>
      <li><svg viewBox="0 0 12 12"><path d="M1 6.5 4.5 10 11 2" fill="none" stroke="var(--tick)" stroke-width="2"/></svg>Peace of Mind</li>
    </ul>
  </section>

  <aside class="contact-panel">
    <div class="attorney-name">Danielle Varnholt</div>
    <div class="attorney-role">Attorney/Of Counsel</div>
    <ul class="contact-lines">
      <li><svg viewBox="0 0 12 12"><path d="M6 11.5C3 8 2 6.3 2 4.5a4 4 0 0 1 8 0c0 1.8-1 3.5-4 7z" fill="var(--blue)"/><circle cx="6" cy="4.5" r="1.5" fill="var(--panel)"/></svg>4712 Cedarbrook Lane Lakemont, Eastvale 00512</li>
      <li class="phone"><svg viewBox="0 0 12 12"><path d="M3 1h2l1 3-1.5 1a6 6 0 0 0 2.5 2.5L8 6l3 1v2c0 1-1 2-2 2C5 11 1 7 1 3c0-1 1-2 2-2z" fill="var(--blue)"/></svg>(555) 684-1093</li>
      <li><svg viewBox="0 0 12 12"><rect x="1" y="2.5" width="10" height="7" fill="none" stroke="var(--blue)" stroke-width="1"/><path d="M1 2.5 6 6.5 11 2.5" fill="none" stroke="var(--blue)" stroke-width="1"/></svg>dvarnholt@rpvlegalteam.example</li>
      <li><svg viewBox="0 0 12 12"><circle cx="6" cy="6" r="5" fill="none" stroke="var(--blue)" stroke-width="1"/><ellipse cx="6" cy="6" rx="2.2" ry="5" fill="none" stroke="var(--blue)" stroke-width="1"/><path d="M1 6h10M2 3.5h8M2 8.5h8" stroke="var(--blue)" stroke-width="0.8"/></svg>www.rpvlegalteam.example</li>
    </ul>
  </aside>
</article>
</body>
</html>
```